Harlow Chiropractic we would like to design a trifold brochure that highlights our services

We need a Trifold created for our Chiropractic offices that highlights our services and treatments that we offer giving patients a better quality of life . Areas to highlight
conditions can be found on our websites and specialties .www.harlowchiropractic.example
our doctors have over 20 years experience in this field .
they have worked with the Ridgeport falcons and Dr. Ben Harlow is the Clearwater valley college basketball teams main chiropractor.

Target Market(s)

children to elderly

Font styles to use
Serif

Colors
00a990
0255a3

Requirements
Must have
• logo
• contact info
• pics of doctors
• bios of doctors
• location
• services provided
Nice to have
• none
Should not have
• do not use picture on website of staff we have all new staff in office

```html
<!DOCTYPE html>
<html lang="en">
<head>
<meta charset="utf-8">
<title>Harlow Chiropractic – Trifold Brochure</title>
<link href="https://fonts.googleapis.com/css2?family=Cinzel:wght@500;600&family=Didact+Gothic&display=swap" rel="stylesheet">
<style>
  :root{
    --page-bg:#d9d9d9;
    --paper:#ffffff;
    --paper-alt:#f1f2f3;
    --green:#6ab42d;
    --blue:#1a4fa1;
    --ink:#2b2b2b;
    --ink-soft:#444;
  }
  *{box-sizing:border-box;margin:0;padding:0}
  html,body{width:862px;height:1200px;overflow:hidden}
  body{background:var(--page-bg);font-family:"Didact Gothic",sans-serif;color:var(--ink);position:relative}
  .brochure{position:absolute;left:0;top:266px;width:862px;height:668px;background:var(--paper);box-shadow:0 6px 18px rgba(0,0,0,.25);overflow:hidden}
  .header-photos{position:absolute;left:0;top:0;width:862px;height:112px;display:flex}
  .header-photos .photo{flex:1;height:100%}
  .photo-left{background:linear-gradient(120deg,#1d1a12 0%,#6b5a2a 45%,#3a3020 100%)}
  .photo-mid{background:linear-gradient(100deg,#3d3a33 0%,#8d8879 40%,#cfcbc0 60%,#4c4a44 100%)}
  .photo-right{background:linear-gradient(110deg,#27421c 0%,#4e7d2e 45%,#2c5a20 70%,#b88a2a 100%)}
  .header-curve{position:absolute;left:0;top:0}
  .panels{position:absolute;left:0;top:112px;width:862px;height:526px;display:flex}
  .panel{width:287.3px;height:100%;padding:0 16px;overflow:hidden}
  .panel-middle{background:var(--paper-alt)}
  .footer{position:absolute;left:0;bottom:0;width:862px;height:30px;background:var(--blue);display:flex}
  .footer .url{flex:1;display:flex;align-items:center;justify-content:center;gap:7px;color:#fff;font-size:10px;letter-spacing:.2px}
  .globe{width:11px;height:11px}
  .pill{display:inline-block;font-family:"Cinzel",serif;font-weight:600;color:#fff;border-radius:14px;box-shadow:0 0 0 2px #e4eedd}
  .pill-lg{font-size:19px;padding:3px 14px 2px}
  .pill-sm{font-size:11.5px;padding:2px 12px 1px;border-radius:4px 12px 4px 12px}
  .pill-green{background:var(--green)}
  .pill-blue{background:var(--blue)}
  .panel-title{text-align:center;margin-top:-2px}
  .copy{font-size:9.2px;line-height:1.3;text-align:justify;color:var(--ink-soft)}
  .copy p+p{margin-top:7px}
  .services .copy{margin-top:18px}
  .provide-title{font-family:"Cinzel",serif;font-weight:600;color:var(--blue);font-size:15px;margin:14px 0 8px;letter-spacing:.5px}
  .service-list{list-style:none}
  .service-list li{display:flex;align-items:center;gap:9px;font-size:9.6px;line-height:18px;color:var(--ink)}
  .tick{width:9px;height:9px;flex:none}
  .doctor-head{display:flex;gap:10px;margin-top:10px}
  .doctor-photo{width:42px;height:58px;flex:none;background:linear-gradient(180deg,#c9d3dc 0%,#8ea6bd 100%);border:1px solid #ccc}
  .doctor-photo.alt{background:linear-gradient(180deg,#dfe3e6 0%,#c0506a 100%)}
  .doctor-name{text-align:center;margin-top:8px}
  .right .doctor-name{margin-top:4px}
  .lead-on{margin-top:0}
</style>
</head>
<body>
<main class="brochure">
  <div class="header-photos">
    <div class="photo photo-left" role="img" aria-label="Photo of a clinic treatment room with a chiropractic table"></div>
    <div class="photo photo-mid" role="img" aria-label="Photo of a patient lying on a decompression table beside therapy equipment"></div>
    <div class="photo photo-right" role="img" aria-label="Photo of a chiropractor in green scrubs treating a patient"></div>
  </div>
  <svg class="header-curve" width="862" height="114" viewBox="0 0 862 114" aria-hidden="true">
    <path d="M0 58 C 250 128, 560 130, 862 20 L862 114 L0 114 Z" fill="#fff"/>
    <path d="M0 58 C 250 128, 560 130, 862 20" fill="none" stroke="#6ab42d" stroke-width="7"/>
    <path d="M0 66 C 250 134, 560 136, 862 28" fill="none" stroke="#1a4fa1" stroke-width="3"/>
  </svg>

  <div class="panels">
    <section class="panel services">
      <h2 class="panel-title"><span class="pill pill-lg pill-green">Our Services</span></h2>
      <div class="copy">
        <p>It is our objective to provide hands-on health care here in Nashville that supports a family commitment to overall well-being. We provide comfortable, quality chiropractic, and therapy treatment while we strive to give patients relief from pain. In addition, we offer long term corrective care by tending to their unique conditions. Dr. Harlow has the right touch for gentle care and adjustments while working with all ages from infant to elderly in Nashville. We realize each patient has distinct needs and we provide personal care that is proficient and effective.</p>
      </div>
      <h3 class="provide-title">We Provide:</h3>
      <ul class="service-list">
        <li><svg class="tick" viewBox="0 0 10 10"><rect x=".5" y=".5" width="9" height="9" fill="none" stroke="#6ab42d"/><path d="M2 5 L4.3 7.2 L8.5 1.8" fill="none" stroke="#6ab42d" stroke-width="1.3"/></svg>Chiropractic Manipulation and Adjustments</li>
        <li><svg class="tick" viewBox="0 0 10 10"><rect x=".5" y=".5" width="9" height="9" fill="none" stroke="#6ab42d"/><path d="M2 5 L4.3 7.2 L8.5 1.8" fill="none" stroke="#6ab42d" stroke-width="1.3"/></svg>Spinal Decompression</li>
        <li><svg class="tick" viewBox="0 0 10 10"><rect x=".5" y=".5" width="9" height="9" fill="none" stroke="#6ab42d"/><path d="M2 5 L4.3 7.2 L8.5 1.8" fill="none" stroke="#6ab42d" stroke-width="1.3"/></svg>DOT Physicals</li>
        <li><svg class="tick" viewBox="0 0 10 10"><rect x=".5" y=".5" width="9" height="9" fill="none" stroke="#6ab42d"/><path d="M2 5 L4.3 7.2 L8.5 1.8" fill="none" stroke="#6ab42d" stroke-width="1.3"/></svg>Dry Needling</li>
        <li><svg class="tick" viewBox="0 0 10 10"><rect x=".5" y=".5" width="9" height="9" fill="none" stroke="#6ab42d"/><path d="M2 5 L4.3 7.2 L8.5 1.8" fill="none" stroke="#6ab42d" stroke-width="1.3"/></svg>Pain Management Therapy and Rehabilitation</li>
        <li><svg class="tick" viewBox="0 0 10 10"><rect x=".5" y=".5" width="9" height="9" fill="none" stroke="#6ab42d"/><path d="M2 5 L4.3 7.2 L8.5 1.8" fill="none" stroke="#6ab42d" stroke-width="1.3"/></svg>In Office X-Ray</li>
        <li><svg class="tick" viewBox="0 0 10 10"><rect x=".5" y=".5" width="9" height="9" fill="none" stroke="#6ab42d"/><path d="M2 5 L4.3 7.2 L8.5 1.8" fill="none" stroke="#6ab42d" stroke-width="1.3"/></svg>Orthopedic and Neurological Exams</li>
        <li><svg class="tick" viewBox="0 0 10 10"><rect x=".5" y=".5" width="9" height="9" fill="none" stroke="#6ab42d"/><path d="M2 5 L4.3 7.2 L8.5 1.8" fill="none" stroke="#6ab42d" stroke-width="1.3"/></svg>Flexibility Training</li>
        <li><svg class="tick" viewBox="0 0 10 10"><rect x=".5" y=".5" width="9" height="9" fill="none" stroke="#6ab42d"/><path d="M2 5 L4.3 7.2 L8.5 1.8" fill="none" stroke="#6ab42d" stroke-width="1.3"/></svg>Sensory-Motor and Balance Training</li>
        <li><svg class="tick" viewBox="0 0 10 10"><rect x=".5" y=".5" width="9" height="9" fill="none" stroke="#6ab42d"/><path d="M2 5 L4.3 7.2 L8.5 1.8" fill="none" stroke="#6ab42d" stroke-width="1.3"/></svg>Myo-facial Therapy by a licensed CTA</li>
        <li><svg class="tick" viewBox="0 0 10 10"><rect x=".5" y=".5" width="9" height="9" fill="none" stroke="#6ab42d"/><path d="M2 5 L4.3 7.2 L8.5 1.8" fill="none" stroke="#6ab42d" stroke-width="1.3"/></svg>Goal Oriented Care</li>
        <li><svg class="tick" viewBox="0 0 10 10"><rect x=".5" y=".5" width="9" height="9" fill="none" stroke="#6ab42d"/><path d="M2 5 L4.3 7.2 L8.5 1.8" fill="none" stroke="#6ab42d" stroke-width="1.3"/></svg>Corrective Exercises</li>
        <li><svg class="tick" viewBox="0 0 10 10"><rect x=".5" y=".5" width="9" height="9" fill="none" stroke="#6ab42d"/><path d="M2 5 L4.3 7.2 L8.5 1.8" fill="none" stroke="#6ab42d" stroke-width="1.3"/></svg>Nutritional Counseling</li>
        <li><svg class="tick" viewBox="0 0 10 10"><rect x=".5" y=".5" width="9" height="9" fill="none" stroke="#6ab42d"/><path d="M2 5 L4.3 7.2 L8.5 1.8" fill="none" stroke="#6ab42d" stroke-width="1.3"/></svg>Orthotics</li>
        <li><svg class="tick" viewBox="0 0 10 10"><rect x=".5" y=".5" width="9" height="9" fill="none" stroke="#6ab42d"/><path d="M2 5 L4.3 7.2 L8.5 1.8" fill="none" stroke="#6ab42d" stroke-width="1.3"/></svg>Spinal and Postural Screenings</li>
        <li><svg class="tick" viewBox="0 0 10 10"><rect x=".5" y=".5" width="9" height="9" fill="none" stroke="#6ab42d"/><path d="M2 5 L4.3 7.2 L8.5 1.8" fill="none" stroke="#6ab42d" stroke-width="1.3"/></svg>Lifestyle Advice</li>
      </ul>
    </section>

    <section class="panel panel-middle">
      <h2 class="panel-title"><span class="pill pill-lg pill-blue">Our Doctors</span></h2>
      <h3 class="doctor-name"><span class="pill pill-sm pill-green">Dr. Ben Harlow</span></h3>
      <div class="copy">
        <div class="doctor-head">
          <div class="doctor-photo" role="img" aria-label="Portrait photo of Dr. Ben Harlow"></div>
          <p>Since Dr. Harlow was old enough to dream, he knew that he wanted to be a chiropractor. After attending Westfield College of Chiropractic West and fueling his career in chiropractic with the mindset of putting patients first, he has made the</p>
        </div>
        <p class="lead-on">dream of one day owning his own clinic here in Nashville a reality. Keeping a compassionate and supportive mentality, Dr. Ben is very attentive toward each and every patient, allocating a vast range of therapies so that each patient leaves feeling rejuvenated. Not only is Dr. Ben very knowledgeable and experienced, but patients understand after seeing him that it really is all about them. Dr. Harlow has a plan for each of his individual patients that exceeds the lengths many chiropractors fail to maintain because he drives himself to direct and lasting results for his patients.</p>
        <p>"No one leaves this clinic feeling like a number," comments Dr. Ben when asked what he feels sets his clinic apart from all the others in Nashville. "I don't want you to only feel better for a day after you see me. I want you, as my patient, to feel better indefinitely by receiving a successful wellness plan that I have specifically designed for you. Every person that walks through these doors is different. What works for some may not work for others. My goal is to promote healthy habits along with patient therapies so that pain will not be an option."</p>
        <p>This is the difference Harlow Chiropractic brings to the table. Long-lasting results you can feel make every visit seem like a day at the spa. This clinic offers the latest technology so troubled areas are spotted quickly and eliminated. So, come see Dr. Ben and find a plan for wellness. Dr. Ben believes in not only having sympathy for his patients, but more importantly, he has empathy. All of the public, children, and walk-ins are welcomed!</p>
      </div>
    </section>

    <section class="panel right">
      <h3 class="doctor-name"><span class="pill pill-sm pill-green">Dr. Nathan Harlow</span></h3>
      <div class="copy">
        <div class="doctor-head" style="margin-top:8px">
          <div class="doctor-photo alt" role="img" aria-label="Portrait photo of Dr. Nathan Harlow"></div>
          <p>Dr. Nathan Harlow is originally from Michigan. He earned his Bachelors of Science from Lakemont University in Brookfield, NY, and his Doctorate of Chiropractic from Westfield College of Chiropractic West in San Jose, CA. While in San Jose, he completed his internship at Harbor Light Ministry for</p>
        </div>
        <p class="lead-on">developmentally disabled individuals and Helping Hands Network's Community Outreach Program.</p>
        <p>Dr. Nate is an avid lover of sports and a former collegiate football player. Naturally, while at Westfield College of Chiropractic, he was a member of the Sports Council, which participated in many of the athletic events throughout California.</p>
        <p>Upon graduation, Dr. Nate began practicing chiropractic with his brother in Nashville, Tennessee at a well-known, group family practice, specializing in spinal and extremity rehabilitation. Harlow's practice focuses on everyone from children to athletes. His main passion is to educate his patients about how to treat, prevent, and overcome injuries.</p>
        <p>Dr. Nate moved back to the bay area in 2011 where he married his wonderful wife Mara. He went on to open a practice in Millbrook, California which encompassed the knowledge of injuries on current research throughout the medical and chiropractic communities.</p>
        <p>Dr. Nate has now relocated back to Nashville, Tennessee to join his brother at Harlow Chiropractic. Dr. Nate uses a variety of Chiropractic Techniques for treatments to restore proper function for body. He also uses myofascial release, rehabilitation, exercise, nutrition, and physiotherapy to properly treat his patient's conditions.</p>
        <p>Dr. Nate enjoys golf, strength training, reading, hunting, and scuba diving. He is a member of the National Chiropractic Guild. Dr. Nate Harlow is excited about getting to know you, and being an active part in helping you reach your health goals as your Nashville Chiropractor.</p>
      </div>
    </section>
  </div>

  <footer class="footer">
    <div class="url"><svg class="globe" viewBox="0 0 12 12" aria-hidden="true"><circle cx="6" cy="6" r="5.2" fill="none" stroke="#fff" stroke-width="1"/><ellipse cx="6" cy="6" rx="2.2" ry="5.2" fill="none" stroke="#fff" stroke-width=".8"/><path d="M1 6 H11 M2 3.5 H10 M2 8.5 H10" stroke="#fff" stroke-width=".7"/></svg>www.harlowchiropractic.example</div>
    <div class="url"><svg class="globe" viewBox="0 0 12 12" aria-hidden="true"><circle cx="6" cy="6" r="5.2" fill="none" stroke="#fff" stroke-width="1"/><ellipse cx="6" cy="6" rx="2.2" ry="5.2" fill="none" stroke="#fff" stroke-width=".8"/><path d="M1 6 H11 M2 3.5 H10 M2 8.5 H10" stroke="#fff" stroke-width=".7"/></svg>www.harlowchiropractic.example</div>
    <div class="url"><svg class="globe" viewBox="0 0 12 12" aria-hidden="true"><circle cx="6" cy="6" r="5.2" fill="none" stroke="#fff" stroke-width="1"/><ellipse cx="6" cy="6" rx="2.2" ry="5.2" fill="none" stroke="#fff" stroke-width=".8"/><path d="M1 6 H11 M2 3.5 H10 M2 8.5 H10" stroke="#fff" stroke-width=".7"/></svg>www.harlowchiropractic.example</div>
  </footer>
</main>
</body>
</html>
```